PageForge Design Project for lornabethwickes.com.au

Update
PLEASE NOTE ...Coding Required

I need a simple website to display my art. There will be 4 different categories - FloraGrandis (botanical art), Oceanlife, Travel Sketchbook, Portraits. There needs to be room for an introduction to me and my work,photos of my studio and views from here and a description of each individual piece. I will probably display no more than 10 pieces in category. Obviously I need to change photos on a regular basis.

I would also like to include a CoinPort button to be connected to my CoinPort account.

I have already started to do a website on PageForge but am finding it too hard to do.

Thank you

Lorna
Updates

Reason: I have provided a deadline extension as I feel the initial lead up time could be too short. Hope that helps you. Lorna

Dear designers. Thankyou all so much for submitting some beautiful designs. I will spend time this weekend evaluating them but as the closing date is January 19, I will not make final decisions until then.  You have probably received an update by now butI  just want to mention that Coding is required.

Cheers

Lorna

Thank you Designers for your patience.  I have been advised by ArtistHive that I cannot make a decision until the deadline has passed, so will let you know on Saturday.

Thank you.
Lorna.

Target Market(s)

35 to 75 who want to buy art and very personal gifts

Industry/Entity Type

Travel

Requirements
Must have
• Ability to change photos often. Modern, elegant, streamlined
Nice to have
• The colour green, an elegant font - sans serif and definitely not courier; room for a photo of me (maybe), and an interesting headline font
Should not have
• quirky, cartooney, retro.

```html
<!DOCTYPE html>
<html lang="en">
<head>
<meta charset="utf-8">
<title>Lorna Beth Wickes — Art</title>
<link rel="stylesheet" href="https://fonts.googleapis.com/css2?family=Lato:wght@400;700;900&family=Noto+Serif&display=swap">
<style>
  :root {
    --green: #0fc24a;
    --green-light: #22d35c;
    --green-dark: #0aa83c;
    --ink: #222222;
    --text: #666666;
    --muted: #888888;
    --rule: #e4e4e4;
    --page: #f7f7f7;
    --white: #ffffff;
    --footer-dark: #4a4a4a;
    --sans: 'Lato', Arial, sans-serif;
    --serif: 'Noto Serif', Georgia, serif;
  }
  * { box-sizing: border-box; margin: 0; padding: 0; }
  html, body { width: 1200px; height: 2304px; overflow: hidden; }
  body { position: relative; background: var(--page); font-family: var(--sans); color: var(--text); }

  .site-header {
    position: absolute; top: 0; left: 0; width: 1200px; height: 96px;
    background: linear-gradient(to bottom, var(--green-light), var(--green-dark));
    box-shadow: 0 2px 6px rgba(0,0,0,.15);
  }
  .brand {
    position: absolute; left: 35px; top: 30px;
    font-size: 30px; font-weight: 900; color: var(--white); letter-spacing: -0.5px;
  }
  .brand small { font-size: 17px; font-weight: 400; }
  .main-nav { position: absolute; left: 543px; top: 42px; display: flex; gap: 38px; }
  .main-nav a { color: var(--white); text-decoration: none; font-size: 17px; }

  .intro {
    position: absolute; top: 96px; left: 0; width: 1200px; height: 442px;
    background: var(--white); border-bottom: 1px solid var(--rule); text-align: center;
  }
  .intro-kicker { margin-top: 88px; font-size: 21px; color: var(--ink); letter-spacing: 1px; }
  .intro-name { margin-top: 2px; font-size: 58px; font-weight: 900; color: var(--ink); letter-spacing: 0.5px; line-height: 1.1; }
  .intro-text {
    width: 940px; margin: 28px auto 0; font-family: var(--serif);
    font-size: 19px; line-height: 34px; color: var(--muted);
  }

  .works-bar {
    position: absolute; top: 580px; left: 35px; width: 1130px; height: 70px;
    border-bottom: 1px solid var(--rule);
  }
  .works-title { position: absolute; left: 0; top: 10px; font-size: 23px; font-weight: 700; color: var(--ink); }
  .works-tabs { position: absolute; left: 455px; top: 14px; display: flex; }
  .works-tabs a {
    position: relative; padding: 0 26px; height: 56px; font-size: 17px;
    color: var(--muted); text-decoration: none;
  }
  .works-tabs a.active::after {
    content: ""; position: absolute; left: 0; right: 0; bottom: 0; height: 2px; background: var(--green);
  }

  .gallery {
    position: absolute; top: 695px; left: 35px; width: 1130px;
    display: grid; grid-template-columns: repeat(4, 266px); column-gap: 22px; row-gap: 31px;
  }
  .art-card { height: 509px; background: var(--white); border: 1px solid #dddddd; box-shadow: 0 1px 3px rgba(0,0,0,.12); }
  .art-image {
    height: 292px;
    background: radial-gradient(circle at 52% 40%, #f07a6e 0, #f2938a 28%, #ecc8c2 52%, #e8e6e6 75%);
  }
  .art-body { padding: 16px 26px 0; }
  .art-title { font-size: 20px; font-weight: 700; color: var(--ink); }
  .art-subtitle { margin-top: 4px; font-size: 15px; font-weight: 700; color: var(--green); }
  .art-text { margin-top: 12px; font-size: 14.5px; line-height: 25px; color: var(--muted); }

  .site-footer {
    position: absolute; top: 1801px; left: 0; width: 1200px; height: 388px;
    background: linear-gradient(to bottom, var(--white), #eeeeee);
    border-top: 1px solid var(--rule);
  }
  .footer-col { position: absolute; top: 60px; width: 260px; font-size: 14px; line-height: 25px; color: var(--text); }
  .footer-col h3 { font-size: 17px; font-weight: 700; color: var(--ink); margin-bottom: 22px; letter-spacing: 0.3px; }
  .footer-col h3.footer-brand { font-size: 28px; font-weight: 900; margin-top: -8px; margin-bottom: 14px; }
  .footer-col a { color: var(--green); text-decoration: none; }
  .more-link { display: block; margin-top: 24px; font-weight: 700; }
  .post p { margin-bottom: 6px; }
  .post time { display: block; font-size: 13px; color: var(--muted); margin-bottom: 26px; }
  .photo-grid { display: grid; grid-template-columns: repeat(3, 67px); column-gap: 29px; row-gap: 29px; }
  .photo-thumb { width: 67px; height: 67px; border: 3px solid var(--white); box-shadow: 0 1px 3px rgba(0,0,0,.25); }
  .contact p { margin-bottom: 14px; }
  .social { display: flex; gap: 15px; margin-top: 2px; }
  .social span { width: 21px; height: 21px; border-radius: 50%; background: var(--green); }
  .social span.dark { background: #222222; }

  .copyright {
    position: absolute; top: 2189px; left: 0; width: 1200px; height: 115px;
    background: var(--footer-dark); color: #dddddd; text-align: center;
    font-size: 14px; line-height: 25px; padding-top: 42px;
  }
</style>
</head>
<body>
  <header class="site-header">
    <div class="brand">LORNABETHWICKES<small>.com</small></div>
    <nav class="main-nav">
      <a href="#">HOME</a><a href="#">ABOUT</a><a href="#">GALLERY</a><a href="#">CONTACT</a><a href="#">CART</a>
    </nav>
  </header>

  <section class="intro">
    <p class="intro-kicker">I AM</p>
    <h1 class="intro-name">LORNA BETH WICKES</h1>
    <p class="intro-text">Donec tincidunt imperdiet enim quis aliquet. Cum sociis natoque penatibus et magnis dis parturient montes, nascetur ridiculus mus. Quisque ornare molestie diam eu ullamcorper. Quisque sed malesuada nulla. Mauris eu leo sit amee ornare molestie diam eu t mauris auctor accumsan. Cum sociis natoque penatibus et magnis dis parturient.</p>
  </section>

  <div class="works-bar">
    <h2 class="works-title">MY WORKS</h2>
    <nav class="works-tabs">
      <a href="#">FLORAGRANDIS</a>
      <a href="#" class="active">OCEANLIFE</a>
      <a href="#">TRAVEL SKETCHBOOK</a>
      <a href="#">PORTRAITS</a>
    </nav>
  </div>

  <main class="gallery">
    <article class="art-card"><div class="art-image" role="img" aria-label="Botanical painting of a coral-pink flower"></div><div class="art-body"><h3 class="art-title">Title of the image</h3><p class="art-subtitle">Subtitle goes here</p><p class="art-text">Vestibulum viverra porttitor hendrerit. Nam dictum congue aliquam. Aliquam tristiqum dictum congue aliquam.</p></div></article>
    <article class="art-card"><div class="art-image" role="img" aria-label="Botanical painting of a coral-pink flower"></div><div class="art-body"><h3 class="art-title">Title of the image</h3><p class="art-subtitle">Subtitle goes here</p><p class="art-text">Vestibulum viverra porttitor hendrerit. Nam dictum congue aliquam. Aliquam tristiqum dictum conguem aliquam .</p></div></article>
    <article class="art-card"><div class="art-image" role="img" aria-label="Botanical painting of a coral-pink flower"></div><div class="art-body"><h3 class="art-title">Title of the image</h3><p class="art-subtitle">Subtitle goes here</p><p class="art-text">Vestibulum viverra porttitor hendrerit. Nam dictum congue aliquam. Aliquam tristiqum dictum conguea</p></div></article>
    <article class="art-card"><div class="art-image" role="img" aria-label="Botanical painting of a coral-pink flower"></div><div class="art-body"><h3 class="art-title">Title of the image</h3><p class="art-subtitle">Subtitle goes here</p><p class="art-text">Vestibulum viverra porttitor hendrerit. Nam dictum congue aliquam. Aliquam tristiqum dictum congue aliquistique massa .</p></div></article>
    <article class="art-card"><div class="art-image" role="img" aria-label="Botanical painting of a coral-pink flower"></div><div class="art-body"><h3 class="art-title">Title of the image</h3><p class="art-subtitle">Subtitle goes here</p><p class="art-text">Vestibulum viverra porttitor hendrerit. Nam dictum congue aliquam. Aliquam tristiqum dictum congue aliquam.</p></div></article>
    <article class="art-card"><div class="art-image" role="img" aria-label="Botanical painting of a coral-pink flower"></div><div class="art-body"><h3 class="art-title">Title of the image</h3><p class="art-subtitle">Subtitle goes here</p><p class="art-text">Vestibulum viverra porttitor hendrerit. Nam dictum congue aliquam. Aliquam tristiqum dictum conguem aliquam .</p></div></article>
    <article class="art-card"><div class="art-image" role="img" aria-label="Botanical painting of a coral-pink flower"></div><div class="art-body"><h3 class="art-title">Title of the image</h3><p class="art-subtitle">Subtitle goes here</p><p class="art-text">Vestibulum viverra porttitor hendrerit. Nam dictum congue aliquam. Aliquam tristiqum dictum conguea</p></div></article>
    <article class="art-card"><div class="art-image" role="img" aria-label="Botanical painting of a coral-pink flower"></div><div class="art-body"><h3 class="art-title">Title of the image</h3><p class="art-subtitle">Subtitle goes here</p><p class="art-text">Vestibulum viverra porttitor hendrerit. Nam dictum congue aliquam. Aliquam tristiqum dictum congue aliquistique massa .</p></div></article>
  </main>

  <footer class="site-footer">
    <div class="footer-col" style="left:35px;">
      <h3 class="footer-brand">LORNABETHWICKES</h3>
      <p>Your about us information would fit here nicely. You could also just have an overview and use the link below to link to you full about us page.</p>
      <a href="#" class="more-link">Find out more...</a>
    </div>
    <div class="footer-col" style="left:326px;">
      <h3>CHIRPER FEED</h3>
      <div class="post"><p>Class aptent taciti <a href="#">@sociosqu</a> ad litora torquent per conubia nostra, per inceptos himenaeos</p><time>1 day ago</time></div>
      <div class="post"><p>Class aptent taciti <a href="#">@sociosqu</a> ad litora torquent per conubia nostra, per inceptos himenaeos</p><time>1 day ago</time></div>
    </div>
    <div class="footer-col" style="left:612px;">
      <h3>PHOTOSTREAM FEED</h3>
      <div class="photo-grid">
        <div class="photo-thumb" role="img" aria-label="Building under blue sky" style="background:linear-gradient(#5d8fc9,#a08a6c);"></div>
        <div class="photo-thumb" role="img" aria-label="Pink flower close-up" style="background:linear-gradient(#d93a5c,#f0b23a);"></div>
        <div class="photo-thumb" role="img" aria-label="Row of colourful beach huts" style="background:linear-gradient(90deg,#d94a3a,#f2c23a,#4aa05a);"></div>
        <div class="photo-thumb" role="img" aria-label="Dark textured object" style="background:linear-gradient(#3a2e28,#9a7a5c);"></div>
        <div class="photo-thumb" role="img" aria-label="Harbour view under blue sky" style="background:linear-gradient(#4a86cf,#8a8a8a);"></div>
        <div class="photo-thumb" role="img" aria-label="Figures against yellow wall" style="background:linear-gradient(#c9a83a,#3a3226);"></div>
      </div>
    </div>
    <div class="footer-col contact" style="left:900px;">
      <h3>CONTACT ME</h3>
      <p>Donec id lobortis nibh. Phasellus eget lorem id nisl consequtris nibh.</p>
      <p>My Office<br>The street name<br>Town name , 3265415</p>
      <p>Phone - 1800-555-0192<br>Email - hello@lornabethwickes.com.au</p>
      <div class="social" aria-label="Social links">
        <span></span><span></span><span></span><span class="dark"></span><span></span>
      </div>
    </div>
  </footer>

  <div class="copyright">Copyright © 2012 lornabethwickes.com<br>All rights reserved</div>
</body>
</html>
```